New world-class investment firm needs a business card design

We need a business card design for a new investment firm called 'Ashgrove Capital Partners.' We acquire companies in the media sector and secure funding from conservative ultra, high-net worth individuals. We would like a black and white color design. We are seeking classic, elegant, and sophisticated designs. The final design should communicate financial safety, class, timelessness, and highly ethical. On the back of the business card, we would simply like the lion logo to be centered. I have attached a mock card, and variations on it are welcomed.
Conservative
- Garamond

```html
<!DOCTYPE html>
<html lang="en">
<head>
<meta charset="utf-8">
<title>Ashgrove Capital Partners — Business Card</title>
<link rel="stylesheet" href="https://fonts.googleapis.com/css2?family=EB+Garamond:wght@400;500&display=swap">
<style>
  :root {
    --page: #ffffff;
    --card-black: #050505;
    --card-glow: #2a2a2a;
    --ink-white: #f4f4f4;
    --ink-soft: #d8d8d8;
    --bar-white: #ffffff;
    --icon-dark: #111111;
  }
  * { margin: 0; padding: 0; box-sizing: border-box; }
  html, body {
    width: 1200px;
    height: 499px;
    overflow: hidden;
    background: var(--page);
  }
  .canvas {
    position: relative;
    width: 1200px;
    height: 499px;
    font-family: "EB Garamond", Garamond, serif;
    color: var(--ink-white);
  }
  .card {
    position: absolute;
    top: 100px;
    width: 525px;
    height: 300px;
    background: var(--card-black);
    overflow: hidden;
  }
  .card--front { left: 50px; }
  .card--back  { left: 625px; }

  /* front */
  .front-texture {
    position: absolute;
    inset: 0;
    background: radial-gradient(ellipse 70% 80% at 25% 35%, var(--card-glow) 0%, var(--card-black) 70%);
  }
  .brand-mark {
    position: absolute;
    left: 60px;
    top: 30px;
    width: 60px;
    height: 60px;
    border: 2px solid var(--ink-white);
    border-radius: 50%;
  }
  .brand-name {
    position: absolute;
    left: 26px;
    top: 112px;
    font-size: 25px;
    font-weight: 400;
    white-space: nowrap;
  }
  .brand-cities {
    position: absolute;
    left: 28px;
    top: 148px;
    font-size: 15px;
    color: var(--ink-soft);
    white-space: nowrap;
  }
  .person-name {
    position: absolute;
    left: 300px;
    top: 28px;
    width: 200px;
    text-align: center;
    font-size: 22px;
    white-space: nowrap;
  }
  .person-title {
    position: absolute;
    left: 300px;
    top: 60px;
    width: 200px;
    text-align: center;
    font-size: 15px;
    color: var(--ink-soft);
  }
  .contact-bar {
    position: absolute;
    left: 300px;
    top: 150px;
    width: 24px;
    height: 118px;
    background: var(--bar-white);
  }
  .contact-bar svg {
    position: absolute;
    left: 4px;
    width: 16px;
    height: 16px;
  }
  .contact-bar .icon-mail  { top: 10px; }
  .contact-bar .icon-phone { bottom: 10px; }
  .contact-email {
    position: absolute;
    left: 334px;
    top: 164px;
    font-size: 12px;
    white-space: nowrap;
  }
  .contact-phone {
    position: absolute;
    left: 334px;
    top: 240px;
    font-size: 20px;
    white-space: nowrap;
  }

  /* back */
  .back-glow {
    position: absolute;
    inset: 0;
    background: radial-gradient(circle at 50% 50%, var(--card-glow) 0%, var(--card-black) 60%);
  }
  .back-lockup {
    position: absolute;
    left: 0;
    right: 0;
    top: 50%;
    transform: translateY(-50%);
    display: flex;
    align-items: center;
    justify-content: center;
    gap: 14px;
  }
  .back-lockup .lockup-circle {
    width: 30px;
    height: 30px;
    border: 2px solid var(--ink-white);
    border-radius: 50%;
  }
  .back-lockup .lockup-name {
    font-size: 26px;
    white-space: nowrap;
  }
</style>
</head>
<body>
<main class="canvas">

  <section class="card card--front" aria-label="Business card front">
    <div class="front-texture" role="img" aria-label="Faint tonal background pattern"></div>
    <div class="brand-mark"></div>
    <p class="brand-name">Ashgrove Capital Partners</p>
    <p class="brand-cities">New York • Los Angels • Geneva</p>

    <p class="person-name">Julian T. Harrow</p>
    <p class="person-title">Chairman &amp; CEO</p>

    <div class="contact-bar">
      <svg class="icon-mail" viewBox="0 0 16 16" aria-hidden="true">
        <rect x="1.5" y="3.5" width="13" height="9" fill="none" stroke="var(--icon-dark)" stroke-width="1.4"/>
        <path d="M1.5 3.5 L8 9 L14.5 3.5" fill="none" stroke="var(--icon-dark)" stroke-width="1.4"/>
      </svg>
      <svg class="icon-phone" viewBox="0 0 16 16" aria-hidden="true">
        <rect x="4" y="1" width="8" height="14" rx="1.5" fill="var(--icon-dark)"/>
        <rect x="5.5" y="3" width="5" height="6" fill="var(--bar-white)"/>
        <circle cx="8" cy="12" r="1" fill="var(--bar-white)"/>
      </svg>
    </div>
    <p class="contact-email">julian@ashgrovecap.com</p>
    <p class="contact-phone">917.555.0148</p>
  </section>

  <section class="card card--back" aria-label="Business card back">
    <div class="back-glow"></div>
    <div class="back-lockup">
      <span class="lockup-circle"></span>
      <span class="lockup-name">Ashgrove Capital Partners</span>
    </div>
  </section>

</main>
</body>
</html>
```